Zielgruppe
Kauf, Vermietung, Bewirtschaftung und Optimierung von Wohnimmobilien. Zielgruppe sind Immobilienmakler, Banken und private Hausverkäufer.
Aufgabenstellung
Als Vorgabe möchte ich das nicht bestimmen, jedoch würde ich als Farbwahl blau-weiß oder etwas in die maritime Richtung bevorzugen.

```html
<!DOCTYPE html>
<html lang="de">
<head>
<meta charset="utf-8">
<title>Linden Habitat – Geschäftsausstattung</title>
<link rel="stylesheet" href="https://fonts.googleapis.com/css2?family=Jost:wght@300;400&display=swap">
<style>
  :root {
    --brand-blue: #0072bc;
    --brand-blue-light: #5ea6d8;
    --ink: #1d1d1b;
    --paper: #ffffff;
    --frame: #3a3a3a;
  }
  * { margin: 0; padding: 0; box-sizing: border-box; }
  html, body {
    width: 972px; height: 1200px; overflow: hidden;
    background: var(--paper);
    font-family: "Jost", "Futura", sans-serif;
    font-weight: 300;
    color: var(--ink);
  }
  .canvas { position: relative; width: 972px; height: 1200px; }

  .wordmark { color: var(--brand-blue); font-weight: 300; white-space: nowrap; letter-spacing: 0.01em; }

  .hero-mark { position: absolute; left: 70px; top: 68px; font-size: 104px; line-height: 1; }

  /* Letterhead */
  .letterhead {
    position: absolute; left: 75px; top: 397px; width: 557px; height: 784px;
    border: 1px solid var(--frame); overflow: hidden; background: var(--paper);
  }
  .letterhead__mark { position: absolute; right: 48px; top: 38px; font-size: 26px; line-height: 1; }
  .letterhead__sender { position: absolute; left: 31px; top: 163px; font-size: 7.5px; }
  .letterhead__sender .wordmark { font-size: inherit; }
  .letterhead__skyline { position: absolute; left: -42px; top: 640px; width: 192px; height: 192px; }
  .letterhead__footer {
    position: absolute; top: 716px; width: 140px;
    font-size: 7.3px; line-height: 9px;
  }
  .letterhead__footer--left { left: 184px; }
  .letterhead__footer--right { left: 348px; }

  /* Business cards */
  .card {
    position: absolute; left: 672px; width: 275px; height: 163px;
    overflow: hidden;
  }
  .card--front { top: 600px; border: 1px solid var(--frame); background: var(--paper); }
  .card--back { top: 800px; background: var(--brand-blue); color: var(--paper); }

  .card__mark { position: absolute; right: 16px; top: 22px; font-size: 22px; line-height: 1; }
  .card__name {
    position: absolute; left: 118px; top: 82px;
    font-size: 15px; color: var(--brand-blue); line-height: 1;
  }
  .card__role { position: absolute; left: 119px; top: 99px; font-size: 7.5px; color: var(--ink); }
  .card__skyline { position: absolute; left: 8px; top: 100px; width: 92px; height: 92px; }

  .card__details {
    position: absolute; left: 0; right: 0; top: 22px;
    text-align: center; font-size: 7.5px; line-height: 9.5px;
  }
  .card__scene {
    position: absolute; left: 70px; top: 84px; width: 150px; height: 79px;
    background: linear-gradient(180deg, var(--brand-blue) 0%, var(--brand-blue-light) 100%);
  }
</style>
</head>
<body>
<main class="canvas">

  <div class="hero-mark wordmark">Linden Habitat</div>

  <section class="letterhead" aria-label="Briefbogen">
    <div class="letterhead__mark wordmark">Linden Habitat</div>
    <p class="letterhead__sender"><span class="wordmark">Linden Habitat</span> - Fährweg 12 - 24100 Kielsand</p>

    <svg class="letterhead__skyline" viewBox="0 0 100 100" role="img" aria-label="Kreis mit Silhouette einer Hafenstadt mit Fernsehturm, Kirchtürmen und Brücke">
      <circle cx="50" cy="50" r="50" fill="var(--brand-blue)"/>
    </svg>

    <p class="letterhead__footer letterhead__footer--left">Dies ist ein Mustertext. Hier stehen die Angaben wie Adresse, Telefon, Banken HRB usw. usw.. Blindtext und so.</p>
    <p class="letterhead__footer letterhead__footer--right">Dies ist ein Mustertext. Hier stehen die Angaben wie Adresse, Telefon, Banken HRB usw. usw.. Blindtext und so.</p>
  </section>

  <section class="card card--front" aria-label="Visitenkarte Vorderseite">
    <div class="card__mark wordmark">Linden Habitat</div>
    <p class="card__name">Jonas Brenner</p>
    <p class="card__role">Geschäftsführer</p>
    <svg class="card__skyline" viewBox="0 0 100 100" role="img" aria-label="Kreis mit Silhouette einer Hafenstadt">
      <circle cx="50" cy="50" r="50" fill="var(--brand-blue)"/>
    </svg>
  </section>

  <section class="card card--back" aria-label="Visitenkarte Rückseite">
    <p class="card__details">Dies ist ein Mustertext. Hier stehen die Angaben wie Adresse,<br>Telefon, Banken<br>HRB usw. usw.. Blindtext und so.</p>
    <div class="card__scene" role="img" aria-label="Weiße Silhouette einer Hafenstadt mit Fernsehturm, Kirchtürmen, Brücke und Schiff"></div>
  </section>

</main>
</body>
</html>
```